Brochure Projecct

I need a brochure created for my company, which will be sent to customers via email in PDF format. I have uploaded the company logo with this project, which I want incorporated in the design.

Designers should view the company website at www.brightcounselpages.com. I want the brochure to compliment the website (i.e., very clean design). I would also like pictures added to the brochure to make the design visually stunning.

In terms of content, I need four pages in the brochure to add four separate sections of content (one section per page). The four sections of content will be as follows (1) Search Engine Optimization Benefits (2) Increased Client Retention (3) Showcase Your Law Firm (4) Maximize Your Online ROI (5) Pricing Plans. I will give the content to the winning designer to add to the project. Each individual content section will have four subsection titles after which content of approximately 100 to 200 words will appear.

Designers can decide if other pages should be added to the brochure (i.e., a "cover page" that would have little content, but be visually appealing like the cover of a book - - - a "back page" that may just have the logo, contact information, etc).

My company address and email address should be prominently featured through every page (address: 2715 West Juniper Avenue, Suite 1400, Scottsdale, Arizona 85317; email: sales@brightcounselpages.com).

Industry/Entity Type

It Company

Requirements
Must have
• Clean look but visually stunning incorporating the design of the website at brightcounselpages.com as well as the logo. Also, room for content as set forth in the description of this project.

```html
<!DOCTYPE html>
<html lang="en">
<head>
<meta charset="utf-8">
<title>Bright Counsel Pages – Brochure</title>
<link href="https://fonts.googleapis.com/css2?family=Arimo:wght@400;700&display=swap" rel="stylesheet">
<style>
  :root {
    --canvas: #e9ebee;
    --paper: #ffffff;
    --brand: #3f66a8;
    --brand-strip: rgba(63, 102, 168, 0.82);
    --accent-bar: #a9b8d1;
    --ink: #4d4f53;
    --ink-soft: #6a6d72;
    --logo-wash: #eef2f7;
  }
  * { box-sizing: border-box; margin: 0; padding: 0; }
  html, body { width: 1200px; height: 1000px; overflow: hidden; }
  body {
    background: var(--canvas);
    font-family: "Arimo", Arial, sans-serif;
    color: var(--ink);
    position: relative;
  }
  .page {
    position: absolute;
    width: 360px;
    height: 460px;
    background: var(--paper);
    overflow: hidden;
    box-shadow: 0 2px 8px rgba(0,0,0,0.12);
  }
  .pos-1 { left: 30px;  top: 27px; }
  .pos-2 { left: 420px; top: 27px; }
  .pos-3 { left: 810px; top: 27px; }
  .pos-4 { left: 30px;  top: 513px; }
  .pos-5 { left: 420px; top: 513px; }
  .pos-6 { left: 810px; top: 513px; }

  /* shared pieces */
  .photo { position: absolute; }
  .accent-bar { position: absolute; background: var(--accent-bar); }
  .address {
    position: absolute;
    font-size: 7px;
    line-height: 10px;
    text-align: right;
    color: var(--ink-soft);
  }

  /* content pages */
  .section-page .photo { left: 0; top: 0; width: 190px; height: 350px; }
  .title-strip {
    position: absolute;
    left: 190px; top: 0;
    width: 20px; height: 350px;
    background: var(--brand-strip);
    display: flex; align-items: center; justify-content: center;
  }
  .title-strip h2 {
    writing-mode: vertical-rl;
    transform: rotate(180deg);
    color: #fff;
    font-size: 9px;
    font-weight: 400;
    letter-spacing: 0.6px;
    text-transform: uppercase;
    white-space: nowrap;
  }
  .section-page .accent-bar { left: 190px; top: 350px; width: 14px; height: 110px; }
  .section-page .address { left: 14px; top: 378px; width: 166px; }
  .copy {
    position: absolute;
    left: 220px; top: 14px;
    width: 130px;
  }
  .copy h3 {
    color: var(--brand);
    font-size: 10px;
    font-weight: 400;
    text-transform: uppercase;
    margin-bottom: 3px;
  }
  .copy p {
    font-size: 7px;
    line-height: 9.6px;
    margin-bottom: 12px;
  }

  /* brand name in place of logo */
  .brand {
    display: flex; align-items: center; gap: 8px;
  }
  .brand-dot {
    width: 26px; height: 26px; border-radius: 50%;
    background: var(--brand);
    flex: none;
  }
  .brand-name {
    font-size: 17px;
    font-weight: 700;
    line-height: 19px;
    color: var(--brand);
  }

  /* cover */
  .cover .logo-panel {
    position: absolute;
    left: 0; top: 150px;
    width: 190px; height: 170px;
    background: linear-gradient(90deg, var(--paper), var(--logo-wash));
    display: flex; align-items: center; justify-content: center;
  }
  .cover .photo { left: 190px; top: 0; width: 170px; height: 390px; }
  .cover .site-url {
    position: absolute;
    left: 342px; top: 10px;
    writing-mode: vertical-rl;
    font-size: 5.5px;
    color: var(--ink-soft);
  }
  .cover .accent-bar { left: 176px; top: 330px; width: 14px; height: 130px; }
  .cover .address { left: 14px; top: 390px; width: 154px; }

  /* back page */
  .back .logo-panel {
    position: absolute;
    left: 0; top: 140px;
    width: 210px; height: 170px;
    background: linear-gradient(90deg, var(--paper), var(--logo-wash));
    display: flex; align-items: center; justify-content: center;
  }
  .pricing {
    position: absolute;
    left: 210px; top: 0;
    width: 150px; height: 310px;
    background: var(--brand);
    color: #fff;
    padding: 12px 10px 0 12px;
  }
  .pricing h2 {
    font-size: 10px; font-weight: 400;
    text-transform: uppercase;
    margin-bottom: 6px;
  }
  .price-group { margin-bottom: 14px; }
  .price-row {
    display: flex;
    font-size: 6px; line-height: 8.4px;
  }
  .price-row .label { white-space: nowrap; }
  .price-row .leader {
    flex: 1;
    border-bottom: 1px dotted rgba(255,255,255,0.7);
    margin: 0 2px 2px;
  }
  .back .photo { left: 210px; top: 310px; width: 150px; height: 150px; }
  .back .accent-bar { left: 196px; top: 310px; width: 14px; height: 150px; }
  .back .address { left: 14px; top: 390px; width: 170px; }
</style>
</head>
<body>

<!-- Cover -->
<section class="page cover pos-1">
  <div class="logo-panel">
    <div class="brand"><span class="brand-dot"></span><span class="brand-name">Bright Counsel<br>Pages</span></div>
  </div>
  <div class="photo" role="img" aria-label="Photo of a lawyer in a trench coat walking down courthouse steps between stone columns"
       style="background: linear-gradient(180deg, #c9ccd0 0%, #8d9198 50%, #b9bcc1 100%);"></div>
  <span class="site-url">www.brightcounselpages.com</span>
  <div class="accent-bar"></div>
  <p class="address">2715 West Juniper Avenue,<br>Suite 1400, Scottsdale, Arizona 85317<br>Email: sales@brightcounselpages.com</p>
</section>

<!-- Increased Client Retention -->
<section class="page section-page pos-2">
  <div class="photo" role="img" aria-label="Photo of a lawyer with a briefcase climbing stone steps"
       style="background: linear-gradient(180deg, #8a96a8 0%, #b8c0cc 55%, #d6dbe2 100%);"></div>
  <div class="title-strip"><h2>Increased Client Retention</h2></div>
  <div class="copy">
    <h3>Venit utpat</h3>
    <p>Ut acte vel iusci eum ex feugait accumsan blandit facilisi tation duis autem vel eum iriure dolor in hendrerit vulputate velit esse molestie consequat vel illum dolore eu feugiat nulla facilisis.</p>
    <h3>Feugiamet</h3>
    <p>Qui exer ip ex erate dit wisl ulla consed magnis nonsectet ut wis adiam inci blan hent lum velissed tionsed ex ero dolenim amconse niscit ute feu feuismodo dolorpe raesed tat.</p>
    <p>Equam ad tat, vel augait diat. Liqui tincilique ipsum velissim nonsectet wis acilit nullaorper ipis nibh er, consed dolobore in henim velit quatum dolorpe raessit niscil quate vel dolobor ad delissim zzril.</p>
  </div>
  <div class="accent-bar"></div>
  <p class="address">2715 West Juniper Avenue,<br>Suite 1400, Scottsdale, Arizona 85317<br>Email: sales@brightcounselpages.com</p>
</section>

<!-- Maximize Your Online ROI -->
<section class="page section-page pos-3">
  <div class="photo" role="img" aria-label="Photo of a finger touching a glowing touchscreen button"
       style="background: radial-gradient(ellipse at 50% 40%, #a9a5a6 0%, #5f6877 55%, #3c4658 100%);"></div>
  <div class="title-strip"><h2>Maximize Your Online ROI</h2></div>
  <div class="copy">
    <h3>Venit utpat</h3>
    <p>Ut acte vel iusci eum ex feugait accumsan blandit facilisi tation duis autem vel eum iriure dolor in hendrerit vulputate velit esse molestie consequat vel illum dolore eu feugiat nulla facilisis.</p>
    <h3>Feugiamet</h3>
    <p>Qui exer ip ex erate dit wisl ulla consed magnis nonsectet ut wis adiam inci blan hent lum velissed tionsed ex ero dolenim amconse niscit ute feu feuismodo dolorpe raesed tat.</p>
    <p>Equam ad tat, vel augait diat. Liqui tincilique ipsum velissim nonsectet wis acilit nullaorper ipis nibh er, consed dolobore in henim velit quatum dolorpe raessit niscil quate vel dolobor ad delissim zzril.</p>
  </div>
  <div class="accent-bar"></div>
  <p class="address">2715 West Juniper Avenue,<br>Suite 1400, Scottsdale, Arizona 85317<br>Email: sales@brightcounselpages.com</p>
</section>

<!-- Search Engine Optimization Benefits -->
<section class="page section-page pos-4">
  <div class="photo" role="img" aria-label="Photo of a lawyer carrying a briefcase down courthouse steps"
       style="background: linear-gradient(180deg, #9aa3b1 0%, #5c6779 50%, #a9b1bd 100%);"></div>
  <div class="title-strip"><h2>Search Engine Optimization Benefits</h2></div>
  <div class="copy">
    <h3>Venit utpat</h3>
    <p>Ut acte vel iusci eum ex feugait accumsan blandit facilisi tation duis autem vel eum iriure dolor in hendrerit vulputate velit esse molestie consequat vel illum dolore eu feugiat nulla facilisis.</p>
    <h3>Feugiamet</h3>
    <p>Qui exer ip ex erate dit wisl ulla consed magnis nonsectet ut wis adiam inci blan hent lum velissed tionsed ex ero dolenim amconse niscit ute feu feuismodo dolorpe raesed tat.</p>
    <p>Equam ad tat, vel augait diat. Liqui tincilique ipsum velissim nonsectet wis acilit nullaorper ipis nibh er, consed dolobore in henim velit quatum dolorpe raessit niscil quate vel dolobor ad delissim zzril.</p>
  </div>
  <div class="accent-bar"></div>
  <p class="address">2715 West Juniper Avenue,<br>Suite 1400, Scottsdale, Arizona 85317<br>Email: sales@brightcounselpages.com</p>
</section>

<!-- Showcase Your Law Firm -->
<section class="page section-page pos-5">
  <div class="photo" role="img" aria-label="Photo of a hand striking a wooden judge's gavel on its block"
       style="background: radial-gradient(ellipse at 40% 35%, #8a3f1f 0%, #5a2412 55%, #2e120a 100%);"></div>
  <div class="title-strip"><h2>Showcase Your Law Firm</h2></div>
  <div class="copy">
    <h3>Venit utpat</h3>
    <p>Ut acte vel iusci eum ex feugait accumsan blandit facilisi tation duis autem vel eum iriure dolor in hendrerit vulputate velit esse molestie consequat vel illum dolore eu feugiat nulla facilisis.</p>
    <h3>Feugiamet</h3>
    <p>Qui exer ip ex erate dit wisl ulla consed magnis nonsectet ut wis adiam inci blan hent lum velissed tionsed ex ero dolenim amconse niscit ute feu feuismodo dolorpe raesed tat.</p>
    <p>Equam ad tat, vel augait diat. Liqui tincilique ipsum velissim nonsectet wis acilit nullaorper ipis nibh er, consed dolobore in henim velit quatum dolorpe raessit niscil quate vel dolobor ad delissim zzril.</p>
  </div>
  <div class="accent-bar"></div>
  <p class="address">2715 West Juniper Avenue,<br>Suite 1400, Scottsdale, Arizona 85317<br>Email: sales@brightcounselpages.com</p>
</section>

<!-- Back page / Pricing -->
<section class="page back pos-6">
  <div class="logo-panel">
    <div class="brand"><span class="brand-dot"></span><span class="brand-name">Bright Counsel<br>Pages</span></div>
  </div>
  <div class="pricing">
    <h2>Pricing Plans</h2>
    <div class="price-group">
      <div class="price-row"><span class="label">Header</span><span class="leader"></span><span>00.00</span></div>
      <div class="price-row"><span class="label">Pricing Plans</span><span class="leader"></span><span>00.00</span></div>
      <div class="price-row"><span class="label">Pricing Plans</span><span class="leader"></span><span>00.00</span></div>
      <div class="price-row"><span class="label">Pricing Plans</span><span class="leader"></span><span>00.00</span></div>
      <div class="price-row"><span class="label">Pricing Plans</span><span class="leader"></span><span>00.00</span></div>
      <div class="price-row"><span class="label">Pricing Plans</span><span class="leader"></span><span>00.00</span></div>
      <div class="price-row"><span class="label">Pricing Plans</span><span class="leader"></span><span>00.00</span></div>
    </div>
    <div class="price-group">
      <div class="price-row"><span class="label">Header</span><span class="leader"></span><span>00.00</span></div>
      <div class="price-row"><span class="label">Pricing Plans</span><span class="leader"></span><span>00.00</span></div>
      <div class="price-row"><span class="label">Pricing Plans</span><span class="leader"></span><span>00.00</span></div>
      <div class="price-row"><span class="label">Pricing Plans</span><span class="leader"></span><span>00.00</span></div>
      <div class="price-row"><span class="label">Pricing Plans</span><span class="leader"></span><span>00.00</span></div>
      <div class="price-row"><span class="label">Pricing Plans</span><span class="leader"></span><span>00.00</span></div>
    </div>
    <div class="price-group">
      <div class="price-row"><span class="label">Header</span><span class="leader"></span><span>00.00</span></div>
      <div class="price-row"><span class="label">Pricing Plans</span><span class="leader"></span><span>00.00</span></div>
      <div class="price-row"><span class="label">Pricing Plans</span><span class="leader"></span><span>00.00</span></div>
      <div class="price-row"><span class="label">Pricing Plans</span><span class="leader"></span><span>00.00</span></div>
      <div class="price-row"><span class="label">Pricing Plans</span><span class="leader"></span><span>00.00</span></div>
    </div>
  </div>
  <div class="accent-bar"></div>
  <div class="photo" role="img" aria-label="Photo of a lawyer's hands resting on legal books in warm light"
       style="background: linear-gradient(135deg, #2b1d16 0%, #7a4a22 45%, #c98f4e 70%, #3a2a22 100%);"></div>
  <p class="address">2715 West Juniper Avenue,<br>Suite 1400, Scottsdale, Arizona 85317<br>Email: sales@brightcounselpages.com</p>
</section>

</body>
</html>
```